Boutique winery needs new wine label

mas Verlon is a boutique wine company based in the Clare Valley of South Australia. We are an established brand, best known for our Riesling and Grenache. We plan to launch a new sub brand called Le Doux mas and require a new label that is different from the others we use. It will be used on small batch Riesling and should have a rustic but quality feel. Attached is a small image of the house where the winery is based. The label should incorporate a hand drawn sketch of the house.
Target Market(s)
High end wine consumers with an interest in Riesling
Requirements
Must have
- hand drawn sketch of the house
- the name of the wine Le Doux mas present on the front label
- Vintage (2018) and region (Clare Valley) present on the front label
- Minimal use of colour on the label but would look at embellishments such as gold foil
Nice to have
- A clean, simple style of label, preferably with white background
- Le Doux mas written in script style
Should not have
- mas Verlon written on the front label
- the current mas Verlon logo

```html
<!DOCTYPE html>
<html lang="en">
<head>
<meta charset="utf-8">
<title>Le Doux mas Riesling 2018 Label</title>
<link href="https://fonts.googleapis.com/css2?family=EB+Garamond:wght@400&family=Cormorant+Garamond:wght@500&display=swap" rel="stylesheet">
<style>
  :root {
    --paper: #fbf9ee;
    --gold: #d6b97c;
    --ink: #4a4a4a;
    --sketch-mid: #9a9b95;
    --sketch-light: #e4e3da;
  }
  * { margin: 0; padding: 0; box-sizing: border-box; }
  html, body {
    width: 1200px;
    height: 1200px;
    overflow: hidden;
    background: var(--paper);
  }
  .label {
    position: relative;
    width: 1200px;
    height: 1200px;
    background: var(--paper);
  }
  .label__frame {
    position: absolute;
    inset: 22px;
    border: 3px solid var(--gold);
  }
  .label__house {
    position: absolute;
    left: 50%;
    top: 245px;
    width: 380px;
    height: 240px;
    transform: translateX(-50%);
    background: linear-gradient(180deg, var(--sketch-light) 0%, var(--sketch-mid) 100%);
  }
  .label__name {
    position: absolute;
    left: 0;
    right: 0;
    top: 572px;
    text-align: center;
    font-family: "EB Garamond", serif;
    font-weight: 400;
    font-size: 68px;
    line-height: 1;
    letter-spacing: 0.02em;
    color: var(--ink);
  }
  .label__variety {
    position: absolute;
    left: 0;
    right: 0;
    top: 697px;
    text-align: center;
    font-family: "Cormorant Garamond", serif;
    font-weight: 500;
    font-size: 30px;
    line-height: 1;
    letter-spacing: 0.42em;
    padding-left: 0.42em;
    color: var(--ink);
  }
  .label__vintage {
    position: absolute;
    left: 0;
    right: 0;
    top: 872px;
    text-align: center;
    font-family: "EB Garamond", serif;
    font-size: 62px;
    line-height: 1;
    font-variant-numeric: oldstyle-nums;
    color: var(--ink);
  }
  .label__region {
    position: absolute;
    left: 0;
    right: 0;
    top: 960px;
    text-align: center;
    font-family: "Cormorant Garamond", serif;
    font-weight: 500;
    font-size: 32px;
    line-height: 1;
    font-variant: small-caps;
    letter-spacing: 0.28em;
    padding-left: 0.28em;
    color: var(--ink);
  }
</style>
</head>
<body>
  <main class="label">
    <div class="label__frame"></div>
    <div class="label__house" role="img" aria-label="Hand-drawn ink sketch of the two-storey ivy-covered winery house"></div>
    <h1 class="label__name">Le Doux mas</h1>
    <p class="label__variety">RIESLING</p>
    <p class="label__vintage">2018</p>
    <p class="label__region">Clare Valley</p>
  </main>
</body>
</html>
```